rk ironcraft business card metallic look

revamp the existing design but want card to have a metalic look to it

Target Market(s)

construction industry

Industry/Entity Type

constrction

Contact Information for Business Card

front of card RK Ironcraft, phone 4165550193, email rk.ironcraftt@veltrano.com and instagram account; rk_ironcraft_

Font styles to use
Other font styles liked:
• masculine

Colors

Designer to choose only greyscale colors for use in the design.

Requirements
Must have
• back side RK Ironcraft then a list of everything : Siding, ACM Panels, Standing Seam,Soffit, Fascia, Gutters,Metal,Alu,inum, Viynyl, Metal Roofs and roof repairs
Nice to have
• I would like to keep the look of the existing card with the metal grids on the front
Should not have
• Need a design in two days

```html
<!DOCTYPE html>
<html lang="en">
<head>
<meta charset="utf-8">
<title>RK Ironcraft – Business Card</title>
<link href="https://fonts.googleapis.com/css2?family=Montserrat:ital,wght@0,400;0,600;0,700;1,400&display=swap" rel="stylesheet">
<style>
  :root {
    --stage: #7d7d7d;
    --steel-dark-1: #0e0e0e;
    --steel-dark-2: #2a2a2a;
    --steel-light-1: #f2f2f2;
    --steel-light-2: #c9c9c9;
    --panel-1: #3c4144;
    --panel-2: #9aa0a4;
    --white: #ffffff;
    --ink: #111111;
    --icon: #d4d4d4;
  }
  * { margin: 0; padding: 0; box-sizing: border-box; }
  html, body { width: 1200px; height: 1200px; overflow: hidden; }
  body {
    background: var(--stage);
    font-family: "Montserrat", sans-serif;
    position: relative;
  }
  .card {
    position: absolute;
    left: 294px;
    width: 612px;
    height: 382px;
    overflow: hidden;
  }
  .card--front {
    top: 199px;
    background:
      repeating-linear-gradient(0deg, rgba(255,255,255,0.025) 0 1px, transparent 1px 3px),
      linear-gradient(160deg, var(--steel-dark-1) 0%, var(--steel-dark-2) 55%, var(--steel-dark-1) 100%);
  }
  .card--back {
    top: 619px;
    background:
      repeating-linear-gradient(0deg, rgba(0,0,0,0.03) 0 1px, transparent 1px 3px),
      linear-gradient(135deg, var(--steel-light-2) 0%, var(--steel-light-1) 45%, var(--steel-light-2) 100%);
  }
  .panel-art {
    position: absolute;
    inset: 0;
    width: 612px;
    height: 382px;
  }
  .brand-name {
    position: absolute;
    font-weight: 700;
    white-space: nowrap;
  }
  .card--front .brand-name {
    left: 30px;
    top: 282px;
    font-size: 25px;
    color: var(--white);
  }
  .contact-list {
    position: absolute;
    left: 252px;
    top: 250px;
    list-style: none;
  }
  .contact-item {
    display: flex;
    align-items: center;
    height: 36px;
    color: var(--white);
    font-size: 20px;
  }
  .contact-item--phone { font-weight: 700; font-size: 22px; }
  .contact-icon {
    width: 22px;
    height: 22px;
    margin-right: 15px;
    flex: none;
  }
  .card--back .brand-name {
    left: 0;
    right: 0;
    top: 100px;
    text-align: center;
    font-size: 52px;
    color: var(--ink);
  }
  .services {
    position: absolute;
    left: 50px;
    right: 50px;
    top: 242px;
    text-align: center;
    font-style: italic;
    font-size: 21px;
    line-height: 29px;
    color: var(--ink);
  }
</style>
</head>
<body>

<section class="card card--front" aria-label="Card front">
  <svg class="panel-art" viewBox="0 0 612 382">
    <defs>
      <linearGradient id="corrugated" x1="0" y1="0" x2="1" y2="0">
        <stop offset="0" stop-color="var(--panel-1)"/>
        <stop offset="0.5" stop-color="var(--panel-2)"/>
        <stop offset="1" stop-color="var(--panel-1)"/>
      </linearGradient>
    </defs>
    <polygon role="img" aria-label="Corrugated metal sheet texture"
             points="329,0 612,0 612,236 579,255 242,45"
             fill="url(#corrugated)" stroke="var(--white)" stroke-width="4" stroke-linejoin="miter"/>
  </svg>

  <div class="brand-name">RK Ironcraft</div>

  <ul class="contact-list">
    <li class="contact-item contact-item--phone">
      <svg class="contact-icon" viewBox="0 0 24 24" aria-hidden="true">
        <circle cx="12" cy="12" r="12" fill="var(--icon)"/>
        <path d="M8.2 6.5l2 2.3-1.2 1.6c.8 1.7 2.2 3.1 3.9 3.9l1.6-1.2 2.3 2-1.3 2c-4.8-.4-8.9-4.5-9.3-9.3z" fill="var(--steel-dark-1)"/>
      </svg>
      416-555-0193
    </li>
    <li class="contact-item">
      <svg class="contact-icon" viewBox="0 0 24 24" aria-hidden="true">
        <rect x="1" y="5" width="22" height="14" fill="var(--icon)"/>
        <path d="M1 5l11 8 11-8M1 19l8-7M23 19l-8-7" fill="none" stroke="var(--steel-dark-1)" stroke-width="1.6"/>
      </svg>
      rk.ironcraftt@veltrano.com
    </li>
    <li class="contact-item">
      <svg class="contact-icon" viewBox="0 0 24 24" aria-hidden="true">
        <circle cx="12" cy="12" r="12" fill="var(--icon)"/>
      </svg>
      rk_ironcraft_
    </li>
  </ul>
</section>

<section class="card card--back" aria-label="Card back">
  <div class="brand-name">RK Ironcraft</div>
  <p class="services">
    Siding | Acm Panels | Standing Seam | Soffit<br>
    | Fascia | Gutters | Metal | Alumunium | Vinyl<br>
    | Metal Roofs | Roof Repairs
  </p>
</section>

</body>
</html>
```